IT Company Web Design: Chatterly, Pipwire, Streamora

This project consists of 2 major parts
1) Business Site  - "KALVERA IT Services" - www.kalvera-it.example
2) Educational Blog and Streamora channel - "TLQ Code" - www.tlqcode.example
The business site powers the education site and are linked together.
Business Site  - "KALVERA IT Services"
===============================
An IT company specializing in IT education, consulting and software development. Those 3 services create a synergistic effect and that is where the "KAL" comes from. I want that to come through.
The "VERA" means radiating in all directions. In the context of KALVERA, it means those 3 services radiating in all direction in the IT industry.
- I want to replace the  web page art for the www.kalvera-it.example site. Right now I am using images from the web page template .
a) Want a big image to replace the current image where the 3 people are in a meeting (currently on my site). I want to convey those 3 services feeding off each other for the IT industry.
b) custom images branded for kalvera for ...
- Training
- Consulting
- Software development
- I attached a zip file with all the KALVERA logo art. I would like the logo in file "LOGO-PROFILE-IMAGE-1.png" to  be converted into a transparent version  since when I use it on my site, it should up with a white square background which is not what I want.
Educational Blog and Streamora channel - "TLQ Code"
=========================================
I require a Streamora Banner for my Streamora Channel - https://streamora.example/c/TLQCode . I will also want to paste the same banner for the header on my website www.tlqcode.example. I want to maintain a consistent look across all my platforms. This includes my TLQ Code Chatterly page: https://www.chatterly.example/tlqcode
and pipwire: https://pipwire.example/tlqcode
The banner/header image(s) has to conform to the image specifications of all those platforms.
I want the TLQ Banner/Header to include the KALVERA company logo at the bottom lower right hand side (in smaller font - almost like a disclaimer) with small text  "powered by KALVERA IT".
I want the TLQ Design to be very colorful as the TLQ Code logo is. So red, yellow, red and blue are colors that I really want. Look at TLQ Code logo for what I mean (attached).  TLQ Code covers the Java programming language (technical blog and Streamora channel) but it aims to cover Java's entire ecosystem. Java gave rise to many other technologies where Java is like the trunk of a tree and the other technologies are the branches and leaves. I really want to convey that aspect "An ecosystem of technology stemming from Java". but I do not want to specifically name any technologies like the Streamora banner is doing right now. I want to move away from that since technologies come and go.
The TLQ stands for "Truly Lasting Questor" and I want the information I provide to help my visitors to become the best TLQ they can be .  So it would be nice to convey the perseverance or an achievement in knowledge just like we have TLQ trophies in sport, I want it to portray that what they learn here will help them reach their goals. This is why there is a trophy in the TLQ Code log.
- I want the banner/header to include the text "TLQ Code" with the same colors as the TLQ Code logo or it could even be just the logo with the banner.
-An image that invites user to subscribe to TLQ Code´s newsletter. Look at my www.tlqcode.example website look at the sign-up form. I want the image to contain those same red, blue, yellow and blue colors like the TLQ Code logo with the word "Newsletter". It has to include the TLQ Code logo as well.

IT. Programming tutorials, consulting and software development
3 page

```html
<!DOCTYPE html>
<html lang="en">
<head>
<meta charset="utf-8">
<title>KALVERA IT Services</title>
<link href="https://fonts.googleapis.com/css2?family=Roboto:wght@400;500;700&display=swap" rel="stylesheet">
<style>
:root{
  --brand:#1f4fe0;
  --brand-deep:#1a3fd0;
  --topbar:#3c72ee;
  --hero:#3367f4;
  --hero-soft:#4a7cf7;
  --ink:#2b2b33;
  --muted:#55555f;
  --grey-bg:#f8f8fb;
  --card-line:#e6e6ee;
  --dot:#e3e6f2;
  --white:#ffffff;
}
*{margin:0;padding:0;box-sizing:border-box}
html,body{width:1200px;height:4124px;overflow:hidden}
body{position:relative;background:var(--white);font-family:'Roboto',sans-serif;color:var(--ink)}
.abs{position:absolute}

.topbar{position:absolute;left:0;top:0;width:1200px;height:29px;background:var(--topbar);color:var(--white);font-size:12px;letter-spacing:.3px}
.topbar .item{position:absolute;top:7px;display:flex;align-items:center;gap:8px}

.header{position:absolute;left:0;top:29px;width:1200px;height:115px;background:var(--white)}
.brand{position:absolute;left:76px;top:40px;display:flex;align-items:center;gap:12px}
.brand-mark{width:26px;height:26px;border-radius:50%;background:var(--brand)}
.brand-name{font-size:26px;font-weight:700;letter-spacing:4px;color:var(--brand)}
.brand-tag{position:absolute;left:158px;top:72px;font-size:9px;font-weight:700;color:var(--ink);letter-spacing:.2px}
.nav{position:absolute;top:51px;font-size:12px;color:var(--ink);letter-spacing:.3px}
.nav.active{left:664px;top:52px;width:62px;height:21px;line-height:21px;text-align:center;background:var(--brand);color:var(--white);border-radius:5px}
.video-btn{position:absolute;left:1097px;top:54px;width:26px;height:18px;border-radius:4px;background:var(--brand)}

.hero{position:absolute;left:0;top:144px;width:1200px;height:660px;background:var(--hero);overflow:hidden}
.pill{position:absolute;width:60px;height:200px;border-radius:30px;background:var(--hero-soft);opacity:.55;transform:rotate(45deg)}
.hero h1{position:absolute;left:78px;top:200px;font-size:41px;line-height:54px;font-weight:700;color:var(--white);letter-spacing:.5px}

.services-title{position:absolute;left:75px;top:902px;display:flex;align-items:center;font-size:40px;font-weight:700;color:var(--brand)}
.services-title .boxed{background:var(--brand);color:var(--white);padding:12px 6px 14px 5px;margin-right:8px}
.services-desc{position:absolute;left:75px;top:1006px;font-size:11px;font-weight:500;line-height:36px;color:var(--ink)}
.art{position:absolute;border-radius:6px}

.card{position:absolute;top:1232px;width:315px;height:275px;background:var(--white);border:1px solid var(--card-line);border-radius:10px;box-shadow:0 3px 6px rgba(0,0,0,.12);text-align:center}
.card .icon{position:absolute;left:50%;top:26px;width:64px;height:64px;margin-left:-32px;border-radius:10px}
.card h3{position:absolute;left:0;right:0;top:152px;font-size:12px;font-weight:700;color:var(--brand)}
.card p{position:absolute;left:20px;right:20px;top:196px;font-size:11px;line-height:36px;color:var(--muted)}
.card .d{position:absolute;width:12px;height:12px;border-radius:50%;background:var(--dot)}

.grey{position:absolute;left:0;top:1635px;width:1200px;height:1175px;background:var(--grey-bg)}
.sq{position:absolute;background:#eef0fb;border-radius:8px}
.section-title{position:absolute;left:182px;font-size:38px;font-weight:700;color:var(--ink)}
.section-title .hl{color:var(--brand-deep)}
.body-text{position:absolute;left:76px;width:1000px;font-size:15px;color:var(--muted);letter-spacing:.1px}
.sectors-label{position:absolute;left:77px;top:1948px;font-size:16px;font-weight:500;color:var(--brand)}
.sector{position:absolute;left:77px;display:flex;align-items:center;gap:14px;font-size:16px;color:var(--muted)}
.sector .ico{width:30px;height:26px}

.feature{position:absolute;width:414px;height:190px;background:var(--white);border-radius:10px;box-shadow:0 2px 6px rgba(0,0,0,.12);overflow:hidden;text-align:center}
.feature h4{height:43px;line-height:43px;background:var(--brand);color:var(--white);font-size:16px;font-weight:500;border-radius:10px 10px 0 0}
.feature p{padding:30px 24px 0;font-size:12.5px;line-height:27px;color:var(--muted);letter-spacing:.2px}
.f-icon{position:absolute;width:54px;height:54px;border-radius:8px}

.premium{position:absolute;left:0;width:1200px;text-align:center}
.btn{position:absolute;left:504px;top:3891px;width:190px;height:39px;line-height:39px;text-align:center;background:var(--brand);color:var(--white);font-size:13px;font-weight:500;border-radius:4px;box-shadow:0 2px 4px rgba(0,0,0,.2)}

.footer{position:absolute;left:0;top:4027px;width:1200px;height:97px;background:var(--brand);color:var(--white);font-size:12px;font-weight:500;text-align:center;line-height:97px;letter-spacing:.2px}
</style>
</head>
<body>

<div class="topbar">
  <div class="item" style="left:102px">
    <svg width="13" height="13" viewBox="0 0 24 24"><path fill="#fff" d="M6.6 10.8a15 15 0 006.6 6.6l2.2-2.2a1 1 0 011-.2 11 11 0 003.5.6 1 1 0 011 1V20a1 1 0 01-1 1A17 17 0 013 4a1 1 0 011-1h3.5a1 1 0 011 1 11 11 0 00.6 3.5 1 1 0 01-.3 1z"/></svg>
    (355) 410-555-017
  </div>
  <div class="item" style="left:420px">
    <svg width="12" height="14" viewBox="0 0 24 28"><path fill="#fff" d="M12 0a10 10 0 00-10 10c0 7.5 10 18 10 18s10-10.5 10-18A10 10 0 0012 0zm0 14a4 4 0 110-8 4 4 0 010 8z"/></svg>
    LUSARIA (MAREVIA ISLES)
  </div>
  <div class="item" style="left:780px">
    <svg width="15" height="11" viewBox="0 0 24 18"><path fill="#fff" d="M0 0h24v18H0z M0 1l12 9 12-9" stroke="#3c72ee" stroke-width="2"/></svg>
    INFO@KALVERA-IT.EXAMPLE
  </div>
</div>

<div class="header">
  <div class="brand"><div class="brand-mark"></div><div class="brand-name">KALVERA</div></div>
  <div class="brand-tag">WE PRACTICE WHAT WE TEACH</div>
  <div class="nav active">HOME</div>
  <div class="nav" style="left:746px">EDUCATIONAL BLOG</div>
  <div class="nav" style="left:904px">CONTACT</div>
  <div class="video-btn"></div>
</div>

<section class="hero">
  <div class="pill" style="left:680px;top:-20px"></div>
  <div class="pill" style="left:1090px;top:-10px"></div>
  <div class="pill" style="left:300px;top:280px"></div>
  <div class="pill" style="left:30px;top:360px"></div>
  <div class="pill" style="left:300px;top:400px"></div>
  <h1>FROM EDUCATION TO<br>INNOVATION</h1>
  <svg class="abs" style="left:0;top:0" width="1200" height="660" viewBox="0 0 1200 660">
    <path fill="#fff" d="M0 626 C150 600 260 672 420 648 C560 628 700 500 870 523 C1000 540 1100 610 1200 628 L1200 660 L0 660 Z"/>
  </svg>
</section>

<div class="services-title"><span class="boxed">OUR</span>SERVICES</div>
<div class="services-desc">WE OFFER TRAINING, CONSULTING AND SOFTWARE DEVELOPMENT<br>SERVICES FOR THE I.T SOFTWARE INDUSTRY</div>
<div class="art" role="img" aria-label="Illustration of a team working together around a desk with computers" style="left:509px;top:824px;width:603px;height:288px;background:linear-gradient(180deg,#f4f5fa,#e6e7ee)"></div>

<div class="card" style="left:75px">
  <span class="d" style="left:34px;top:20px"></span><span class="d" style="left:270px;top:55px"></span><span class="d" style="left:42px;top:100px"></span><span class="d" style="left:240px;top:130px"></span><span class="d" style="left:84px;top:138px"></span><span class="d" style="left:26px;top:240px"></span><span class="d" style="left:264px;top:230px"></span>
  <div class="icon" role="img" aria-label="Training illustration" style="width:66px;height:96px;margin-left:-33px;background:linear-gradient(180deg,#f1b33c,#d83a3a)"></div>
  <h3>TRAINING</h3>
  <p>LIVE/REMOTE BASED INSTRUCTOR-LED<br>TRAINING</p>
</div>
<div class="card" style="left:442px">
  <span class="d" style="left:44px;top:20px"></span><span class="d" style="left:280px;top:55px"></span><span class="d" style="left:30px;top:100px"></span><span class="d" style="left:264px;top:138px"></span><span class="d" style="left:36px;top:240px"></span><span class="d" style="left:274px;top:230px"></span>
  <div class="icon" role="img" aria-label="Consulting illustration" style="width:96px;height:80px;margin-left:-48px;background:linear-gradient(180deg,#cfe0ff,#3f6ee0)"></div>
  <h3>CONSULTING</h3>
  <p>ASSIST, ADVICE AND ASSESS YOUR<br>NEEDS</p>
</div>
<div class="card" style="left:808px">
  <span class="d" style="left:44px;top:20px"></span><span class="d" style="left:276px;top:55px"></span><span class="d" style="left:48px;top:100px"></span><span class="d" style="left:250px;top:130px"></span><span class="d" style="left:30px;top:240px"></span><span class="d" style="left:264px;top:230px"></span>
  <div class="icon" role="img" aria-label="Software development illustration" style="width:90px;height:86px;margin-left:-45px;background:linear-gradient(180deg,#7fcf5a,#2f5fd8)"></div>
  <h3>SOFTWARE DEVELOPMENT</h3>
  <p style="top:200px">LET US BUILD YOUR NEXT GREAT IDEA</p>
</div>

<div class="grey">
  <svg class="abs" style="left:0;bottom:0" width="1200" height="140" viewBox="0 0 1200 140">
    <path fill="#fff" d="M0 100 C200 40 380 30 560 50 C780 74 960 20 1200 120 L1200 140 L0 140 Z"/>
  </svg>
</div>
<div class="sq" style="left:1030px;top:1648px;width:40px;height:58px"></div>
<div class="sq" style="left:140px;top:1780px;width:66px;height:100px"></div>
<div class="sq" style="left:492px;top:1982px;width:70px;height:100px"></div>
<div class="sq" style="left:0;top:2198px;width:70px;height:100px"></div>
<div class="sq" style="left:960px;top:2178px;width:72px;height:100px"></div>

<div class="abs" role="img" aria-label="Group of people icon" style="left:77px;top:1677px;width:80px;height:58px;border-radius:8px;background:var(--brand)"></div>
<div class="section-title" style="top:1682px"><span class="hl">WHO</span> WE ARE?</div>
<div class="body-text" style="top:1788px;line-height:36px">KALVERA I.T SERVICES LDA. IS A LUSARIAN BASED COMPANY BASED IN THE MAREVIA ISLES WHICH PROVIDES<br>BOTH DOMESTIC AND INTERNATIONAL I.T BASED SOLUTIONS. &nbsp;KALVERA'S SERVICES SPAN OUT INTO THREE<br>DIFFERENT SECTORS WITHIN THE I.T INDUSTRY.</div>
<div class="sectors-label">THESE SECTORS ARE</div>

<div class="sector" style="top:2072px"><svg class="ico" viewBox="0 0 30 26"><rect x="9" y="2" width="19" height="13" fill="none" stroke="#1f4fe0" stroke-width="2"/><circle cx="5" cy="8" r="3" fill="#1f4fe0"/><rect x="2" y="12" width="6" height="12" fill="#1f4fe0"/></svg>TRAINING</div>
<div class="sector" style="top:2126px"><svg class="ico" viewBox="0 0 30 26"><circle cx="15" cy="6" r="4" fill="#1f4fe0"/><circle cx="5" cy="10" r="3" fill="#1f4fe0"/><circle cx="25" cy="10" r="3" fill="#1f4fe0"/><rect x="2" y="16" width="26" height="4" fill="#1f4fe0"/><rect x="8" y="20" width="3" height="6" fill="#1f4fe0"/><rect x="19" y="20" width="3" height="6" fill="#1f4fe0"/></svg>CONSULTING</div>
<div class="sector" style="top:2179px"><svg class="ico" viewBox="0 0 30 26"><rect x="2" y="2" width="26" height="18" fill="none" stroke="#1f4fe0" stroke-width="2"/><path d="M9 8l-3 3 3 3M21 8l3 3-3 3" stroke="#1f4fe0" stroke-width="2" fill="none"/><rect x="8" y="22" width="14" height="2" fill="#1f4fe0"/></svg>SOFTWARE DEVELOPMENT</div>

<div class="art" role="img" aria-label="Illustration of a busy office worker at a desk with a computer and a wall clock" style="left:720px;top:1909px;width:280px;height:280px;background:linear-gradient(180deg,#eef0f8,#c9cbe0)"></div>

<div class="body-text" style="top:2296px;line-height:45px">HAVING OUR ROOTS FIRMLY PLANTED IN THE TRAINING SECTOR ALLOWS US TO IMPLEMENT INDUSTRY BEST PRACTICES,<br>INTRODUCE CUTTING EDGE TECHNOLOGIES AND OFFER NEW SOLUTIONS INTO OUR SOFTWARE DEVELOPMENT AND<br>CONSULTING SERVICES.</div>
<div class="body-text" style="top:2476px;line-height:45px">OUR EXPERIENCE IN SOFTWARE DEVELOPMENT AND CONSULTING REINFORCE OUR EDUCATIONAL TRAINING SERVICES<br>AS RELEVANT AND APPLICABLE MATERIALS ARE CONSTANTLY IMPROVED. THE OVERALL EFFECT IS THAT ALL THREE OF<br>KALVERA'S SERVICES BENEFIT FROM AN OVERALL SYNERGISTIC EFFECT WHICH IS PAST ON TO YOU.</div>

<svg class="abs" style="left:77px;top:2800px" width="90" height="90" viewBox="0 0 90 90">
  <circle cx="45" cy="45" r="43" fill="#1f4fe0"/>
  <text x="45" y="66" text-anchor="middle" font-family="Roboto, sans-serif" font-weight="700" font-size="58" fill="#fff">?</text>
</svg>
<div class="section-title" style="top:2822px">WHY CHOOSE <span class="hl">US?</span></div>
<div class="body-text" style="top:2935px;line-height:45px">WE HAVE A WIDE RANGE OF EXPERIENCE ACROSS MANY INDUSTRIES SUCH AS SPACE, AVIATION AND FINANCE. WITH<br>OVER 20 YEARS EXPERIENCE ACROSS ALL THESE INDUSTRIES, YOU CLEARLY GAIN TOP VALUE.</div>

<div class="f-icon" role="img" aria-label="Instructor presenting icon" style="left:258px;top:3068px;background:#d9d9de"></div>
<div class="f-icon" role="img" aria-label="Group of consultants icon" style="left:890px;top:3068px;background:#d9d9de"></div>
<div class="feature" style="left:77px;top:3146px"><h4>TOP INDUSTRY TRAINING</h4><p>OFFERING EXPERIENCED AND CERTIFIED INSTRUCTOR<br>TRAINING FOR YOUR I.T SOFTWARE AND DEV OPS<br>TRAINING NEEDS</p></div>
<div class="feature" style="left:710px;top:3146px"><h4>EXPERIENCED CONSULTANTS</h4><p>WE OFFER ON-SITE CONSULTANTS HELPING YOU<br>DEVELOP AND/OR ARCHITECTING YOUR<br>SOFTWARE.</p></div>

<svg class="abs" style="left:251px;top:3403px" width="54" height="54" viewBox="0 0 54 54"><circle cx="27" cy="27" r="25" fill="none" stroke="#222" stroke-width="2.5"/><circle cx="27" cy="25" r="8" fill="#222"/><rect x="23" y="33" width="8" height="7" fill="#222"/></svg>
<div class="f-icon" role="img" aria-label="Pricing document icon" style="left:890px;top:3404px;background:#d9d9de"></div>
<div class="feature" style="left:77px;top:3472px"><h4>CUTTING EDGE</h4><p>WE HAVE THE EXPERIENCE TO BRING YOU INTO THE<br>FUTURE. CLOUD MIGRATION. CONTAINERIZATION AND<br>IMPLEMENTING PROCESS AUTOMATION IN YOUR<br>COMPANY.</p></div>
<div class="feature" style="left:710px;top:3472px"><h4>VARIOUS PRICING OPTIONS</h4><p>SEVERAL DIFFERENT PRICING MODELS THAT<br>BEST FIT YOUR PROJECT</p></div>

<div class="premium" style="top:3774px;font-size:32px;font-weight:700;color:var(--brand)">TRY PREMIUM FOR FREE</div>
<div class="premium" style="top:3832px;font-size:11.5px;font-weight:500;color:var(--ink)">WE PROVIDE 15 DAYS TRIAL TO ALL THE USERS WILLING TO TRY NOVA PREMIUM SERVICES.</div>
<div class="btn">TRY NOW</div>

<div class="footer">COPYRIGHT © 2020 KALVERA IT SERVICES. NOVA BUSINESS | DEVELOPED BY NOVA THEME POWERED BY PAGECRAFT.</div>

</body>
</html>
```